Saffron Lantern Court Business Card

I am looking for a business card desgined for my restaurant. It is an Indian restaurant, we are looking for something thats modern, yet traditional with the indian culture, we are looking for colors that match our logo. The logo is a design of the building with the name of the restaurant. for more information on the restaurant go to www.saffronlanterncourt.example

Industry/Entity Type

Indian Restaurant

Contact Information for Business Card

we are looking for somthing thats modern, yet traditional with the indian culture, we are looking for colors that match our logo. The logo is a design of the building with the name of the restaurant. for more information on the restaurant go to www.saffronlanterncourt.example

Requirements
Must have
• The logo that is attached,
• Name: Harvinder Oberoi,
• address of the restaurant: 7328 West Larkspur Rd, Phoenix, Arizona, 85099
• Phone: (602) 555-0147
• Fax: (602) 555-0193
• Restaurant Catering Banquet
• Website: www.SaffronLanternCourt.example
Nice to have
• wanted to get something that goes with the theme of the restaurant, which is traditional but also keep a very professional and modern touch

```html
<!DOCTYPE html>
<html lang="en">
<head>
<meta charset="utf-8">
<title>Saffron Lantern Court – Business Card</title>
<link href="https://fonts.googleapis.com/css2?family=Arimo:wght@400;700&display=swap" rel="stylesheet">
<style>
  :root {
    --backdrop: #e6e6e6;
    --card: #ffffff;
    --crimson: #9c1a2b;
    --ember: #c8562a;
    --ink-soft: #8a2430;
    --white: #ffffff;
  }
  html, body {
    margin: 0;
    padding: 0;
    width: 1200px;
    height: 997px;
    overflow: hidden;
    background: var(--backdrop);
    font-family: "Arimo", Arial, sans-serif;
  }
  .card {
    position: absolute;
    left: 280px;
    width: 640px;
    height: 366px;
    background: var(--card);
    border-radius: 18px;
    box-shadow: 0 6px 18px rgba(0,0,0,0.18);
    overflow: hidden;
  }
  .card--front { top: 92px; }
  .card--back  { top: 539px; }

  .brand-name {
    position: absolute;
    left: 0;
    right: 0;
    text-align: center;
    color: var(--crimson);
    font-weight: 700;
    text-transform: uppercase;
    letter-spacing: 2px;
    line-height: 1.05;
    margin: 0;
  }
  .card--front .brand-name { top: 92px; font-size: 38px; }
  .card--back .brand-name  { top: 28px; font-size: 30px; }

  .band {
    position: absolute;
    left: 0;
    right: 0;
    background: var(--crimson);
    color: var(--white);
    font-weight: 700;
  }
  .card--front .band {
    top: 282px;
    height: 30px;
    line-height: 30px;
    text-align: center;
    font-size: 15px;
    letter-spacing: 1px;
  }
  .card--back .band {
    top: 166px;
    height: 32px;
    line-height: 32px;
    font-size: 19px;
    letter-spacing: 0.5px;
  }
  .person-name { position: absolute; left: 200px; }
  .person-title {
    position: absolute;
    top: 204px;
    left: 232px;
    margin: 0;
    font-size: 14px;
    color: var(--ink-soft);
  }
  .address {
    position: absolute;
    top: 214px;
    right: 30px;
    margin: 0;
    text-align: right;
    font-style: normal;
    font-size: 15px;
    color: var(--ember);
    line-height: 1.3;
  }
  .address strong {
    display: block;
    color: var(--crimson);
    font-size: 17px;
    letter-spacing: 0.5px;
  }
  .contact-list {
    position: absolute;
    left: 30px;
    bottom: 26px;
    margin: 0;
    padding: 0;
    list-style: none;
  }
  .contact-list li {
    display: flex;
    align-items: center;
    gap: 10px;
    font-size: 16px;
    color: var(--ember);
    height: 26px;
  }
  .contact-icon { width: 18px; height: 18px; flex: none; }
</style>
</head>
<body>

<section class="card card--front" aria-label="Business card front">
  <h1 class="brand-name">Saffron<br>Lantern<br>Court</h1>
  <div class="band">www.saffronlanterncourt.example</div>
</section>

<section class="card card--back" aria-label="Business card back">
  <h2 class="brand-name">Saffron<br>Lantern<br>Court</h2>
  <div class="band"><span class="person-name">HARVINDER OBEROI</span></div>
  <p class="person-title">Marketing Director</p>
  <address class="address">
    <strong>SAFFRON LANTERN COURT</strong>
    7328 West Larkspur Rd, Phoenix<br>
    Arizona, 85099
  </address>
  <ul class="contact-list">
    <li>
      <svg class="contact-icon" viewBox="0 0 18 18" aria-hidden="true">
        <circle cx="9" cy="9" r="9" fill="var(--crimson)"/>
        <path d="M5.5 5 L7.5 4.6 L8.4 7 L7.3 7.8 Q8.2 9.8 10.2 10.7 L11 9.6 L13.4 10.5 L13 12.5 Q7 12.8 5.5 5 Z" fill="var(--white)"/>
      </svg>
      (602) 555-0147
    </li>
    <li>
      <svg class="contact-icon" viewBox="0 0 18 18" aria-hidden="true">
        <circle cx="9" cy="9" r="9" fill="var(--crimson)"/>
        <rect x="6" y="4.5" width="6" height="3" fill="var(--white)"/>
        <rect x="4" y="7.5" width="10" height="4.5" rx="1" fill="var(--white)"/>
        <rect x="6" y="11" width="6" height="2.8" fill="var(--white)" stroke="var(--crimson)" stroke-width="0.6"/>
      </svg>
      (602) 555-0193
    </li>
    <li>
      <svg class="contact-icon" viewBox="0 0 18 18" aria-hidden="true">
        <circle cx="9" cy="9" r="9" fill="var(--crimson)"/>
        <rect x="4.5" y="6" width="9" height="6.5" fill="var(--white)"/>
        <path d="M4.5 6 L9 9.6 L13.5 6" fill="none" stroke="var(--crimson)" stroke-width="0.9"/>
      </svg>
      info@saffronlanterncourt.example
    </li>
  </ul>
</section>

</body>
</html>
```